Golden Pantry Spice

Distributor of seasonings and spices to the restaurant industry.

Industry/Entity Type

Restaurant

Contact Information for Business Card

Golden Pantry
Derek Hollings
TW Brandvik Distributor
316-487-9021
derek@goldpantryspicehub.com

No minimum order
Gluten & MSG free soup bases

```html
<!DOCTYPE html>
<html lang="en">
<head>
<meta charset="utf-8">
<title>Golden Pantry Spice – Business Card</title>
<link rel="stylesheet" href="https://fonts.googleapis.com/css2?family=Open+Sans:wght@400;600;700&display=swap">
<style>
  :root {
    --page-bg: #e6e2dc;
    --card-white: #f7f7f7;
    --card-black: #121212;
    --accent-yellow: #f3e23b;
    --accent-red: #ef5b4b;
    --ink-dark: #2a2a2a;
    --ink-light: #f2f2f2;
    --ink-muted: #cfcfcf;
  }
  html, body {
    margin: 0;
    width: 1200px;
    height: 1023px;
    overflow: hidden;
    background: var(--page-bg);
    font-family: "Open Sans", Arial, sans-serif;
  }
  .card {
    position: absolute;
    left: 75px;
    top: 211px;
    width: 1050px;
    height: 600px;
    background: var(--card-white);
    box-shadow: 0 18px 40px rgba(0,0,0,0.25);
    overflow: hidden;
  }
  .card-art {
    position: absolute;
    inset: 0;
  }
  .brand {
    position: absolute;
    left: 80px;
    top: 165px;
    display: flex;
    align-items: center;
    gap: 18px;
  }
  .brand-mark {
    width: 34px;
    height: 34px;
    border-radius: 50%;
    background: var(--accent-red);
    flex: none;
  }
  .brand-name {
    font-weight: 700;
    font-size: 60px;
    color: var(--ink-dark);
    line-height: 1.05;
  }
  .brand-name span {
    display: block;
  }
  .perks {
    position: absolute;
    left: 52px;
    top: 500px;
    margin: 0;
    padding: 0;
    list-style: none;
    color: var(--ink-light);
    font-weight: 600;
    font-size: 22px;
    line-height: 38px;
  }
  .perks li::before {
    content: "";
    display: inline-block;
    width: 9px;
    height: 9px;
    border-radius: 50%;
    background: var(--accent-red);
    margin-right: 14px;
    vertical-align: middle;
  }
  .contact {
    position: absolute;
    left: 640px;
    top: 250px;
    color: var(--ink-light);
  }
  .contact-name {
    margin: 0;
    font-size: 40px;
    font-weight: 700;
    color: var(--accent-red);
    line-height: 1.1;
  }
  .contact-title {
    margin: 4px 0 30px;
    font-size: 25px;
    color: var(--ink-light);
  }
  .contact-lines {
    margin: 0;
    padding: 0;
    list-style: none;
    font-size: 21px;
    line-height: 40px;
    color: var(--ink-muted);
  }
  .contact-lines li {
    display: flex;
    align-items: center;
    gap: 14px;
  }
  .contact-lines svg {
    width: 22px;
    height: 22px;
    flex: none;
  }
</style>
</head>
<body>
  <div class="card">
    <svg class="card-art" viewBox="0 0 1050 600" aria-hidden="true">
      <path fill="var(--accent-yellow)" transform="translate(-26,-16)"
        d="M640 0 C520 120 560 300 380 400 C250 470 110 460 0 470 L0 600 L1050 600 L1050 0 Z"/>
      <path fill="var(--accent-red)" transform="translate(-13,-8)"
        d="M640 0 C520 120 560 300 380 400 C250 470 110 460 0 470 L0 600 L1050 600 L1050 0 Z"/>
      <path fill="var(--card-black)"
        d="M640 0 C520 120 560 300 380 400 C250 470 110 460 0 470 L0 600 L1050 600 L1050 0 Z"/>
    </svg>

    <div class="brand">
      <span class="brand-mark"></span>
      <span class="brand-name"><span>Golden</span><span>Pantry</span></span>
    </div>

    <ul class="perks">
      <li>No minimum order</li>
      <li>Gluten &amp; MSG free soup bases</li>
    </ul>

    <div class="contact">
      <h1 class="contact-name">Derek Hollings</h1>
      <p class="contact-title">TW Brandvik Distributor</p>
      <ul class="contact-lines">
        <li>
          <svg viewBox="0 0 24 24"><circle cx="12" cy="12" r="12" fill="var(--accent-red)"/><path d="M8 6.5c-.8.8-1 2 .2 4 1.2 2.2 3 4 5.3 5.3 2 1.2 3.2 1 4-.2l-2-2-1.6 1c-1.5-.8-2.8-2.1-3.6-3.6l1-1.6z" fill="var(--card-black)"/></svg>
          316-487-9021
        </li>
        <li>
          <svg viewBox="0 0 24 24"><circle cx="12" cy="12" r="12" fill="var(--accent-red)"/><rect x="6" y="8" width="12" height="8.5" rx="1" fill="var(--card-black)"/><path d="M6.5 8.6 12 13l5.5-4.4" stroke="var(--accent-red)" stroke-width="1.2" fill="none"/></svg>
          derek@goldpantryspicehub.com
        </li>
        <li>
          <svg viewBox="0 0 24 24"><circle cx="12" cy="12" r="12" fill="var(--accent-red)"/><g stroke="var(--card-black)" stroke-width="1.4" fill="none"><circle cx="12" cy="12" r="6.5"/><ellipse cx="12" cy="12" rx="3" ry="6.5"/><path d="M5.5 12h13"/></g></svg>
          www.goldpantryspicehub.com
        </li>
      </ul>
    </div>
  </div>
</body>
</html>
```